Personal Trainer and Corporate Health Business

I need a business card for a new company I'm starting in Australia called "Brisk Vitality Partners" I will be providing a Personal training service as well as corporate health in companies.
The service provided is to help promote an active and healthy lifstyle.
The design should communicate a healthy lifestyle and also the benefits that this can have on a personal level and in the corporate environment and the benefits that flow from that.

Target Market(s)

Members of the public and Corporate

Industry/Entity Type

Environment

Requirements
Must have
• Company logo attached
Look and feel fresh and modern

Tag line: "Actively promoting a healthier lifestyle"

Lewis Norgate
Managing Director

m: 0417 596 304
e: lewis@briskvitalitypartners.com.au

www.briskvitalitypartners.com.au
Nice to have
• Can be 1 or 2 sided

```html
<!DOCTYPE html>
<html lang="en">
<head>
<meta charset="utf-8">
<title>Brisk Vitality Partners – Business Cards</title>
<link rel="stylesheet" href="https://fonts.googleapis.com/css2?family=Arimo:wght@400;700&family=Tinos:wght@400&display=swap">
<style>
  :root {
    --canvas: #d6d6d6;
    --card: #ffffff;
    --brand-blue: #0860b0;
    --text-blue: #1d69b3;
    --rule-blue: #8fb6dc;
    --fresh-green: #a5cd39;
    --white: #ffffff;
  }
  * { margin: 0; padding: 0; box-sizing: border-box; }
  html, body { width: 1200px; height: 900px; overflow: hidden; }
  body {
    position: relative;
    background: var(--canvas);
    font-family: "Arimo", Arial, sans-serif;
  }
  .card {
    position: absolute;
    width: 513px;
    height: 289px;
    background: var(--card);
    border-radius: 14px;
    overflow: hidden;
    box-shadow: 0 1px 3px rgba(0,0,0,0.25);
  }
  .card--appointment { left: 45px; top: 113px; }
  .card--session { left: 45px; top: 466px; }
  .card--front { left: 594px; top: 321px; }

  .reminder__label {
    position: absolute;
    left: 17px;
    top: 163px;
    font-size: 16.5px;
    color: var(--text-blue);
    letter-spacing: 0.3px;
  }
  .reminder__lines {
    position: absolute;
    left: 17px;
    top: 200px;
    width: 198px;
  }
  .reminder__line {
    height: 19px;
    border-bottom: 1px solid var(--rule-blue);
  }
  .reminder__line:first-child { height: 1px; }

  .brand-name {
    position: absolute;
    left: 0;
    width: 100%;
    top: 62px;
    text-align: center;
    font-family: "Tinos", "Times New Roman", serif;
    font-size: 30px;
    text-transform: uppercase;
    letter-spacing: 2px;
    color: var(--brand-blue);
  }
  .front__wave { position: absolute; left: 0; top: 0; }
  .contact {
    position: absolute;
    left: 20px;
    top: 184px;
    color: var(--white);
  }
  .contact__name {
    font-family: "Tinos", "Times New Roman", serif;
    font-size: 20px;
    letter-spacing: 2.4px;
    text-transform: uppercase;
    line-height: 22px;
  }
  .contact__role { font-size: 14px; line-height: 18px; margin-top: 1px; margin-bottom: 4px; }
  .contact__row {
    display: flex;
    align-items: center;
    gap: 8px;
    font-size: 14px;
    letter-spacing: 0.6px;
    line-height: 19.5px;
  }
  .contact__icon { width: 13px; height: 13px; flex: none; }
</style>
</head>
<body>

  <section class="card card--appointment">
    <p class="reminder__label">Next Appointment:</p>
    <div class="reminder__lines">
      <div class="reminder__line"></div><div class="reminder__line"></div>
      <div class="reminder__line"></div><div class="reminder__line"></div>
    </div>
  </section>

  <section class="card card--session">
    <p class="reminder__label">Next Session:</p>
    <div class="reminder__lines">
      <div class="reminder__line"></div><div class="reminder__line"></div>
      <div class="reminder__line"></div><div class="reminder__line"></div>
    </div>
  </section>

  <section class="card card--front">
    <p class="brand-name">Brisk Vitality Partners</p>

    <svg class="front__wave" width="513" height="289" viewBox="0 0 513 289">
      <path d="M0,155 C100,144 200,150 290,184 C200,166 100,164 0,177 Z" fill="var(--fresh-green)"/>
      <path d="M0,178 C120,168 220,172 300,190 C380,206 460,192 513,168 L513,289 L0,289 Z" fill="var(--brand-blue)"/>
      <path id="tagline-path" d="M282,190 C360,198 430,188 492,168" fill="none"/>
      <text font-family="Arimo, Arial, sans-serif" font-size="13.5" fill="var(--brand-blue)" letter-spacing="0.3">
        <textPath href="#tagline-path">Promoting a healthier lifestyle</textPath>
      </text>
    </svg>

    <div class="contact">
      <p class="contact__name">Lewis Norgate</p>
      <p class="contact__role">Personal Trainer &amp; Fitness Consultant</p>
      <p class="contact__row">
        <svg class="contact__icon" viewBox="0 0 13 13"><rect x="0" y="0" width="13" height="13" rx="2" fill="var(--white)"/><rect x="4" y="2" width="5" height="9" rx="1" fill="var(--brand-blue)"/><rect x="5" y="3" width="3" height="6" fill="var(--white)"/></svg>
        0417 596 304
      </p>
      <p class="contact__row">
        <svg class="contact__icon" viewBox="0 0 13 13"><rect x="0" y="0" width="13" height="13" rx="2" fill="var(--white)"/><rect x="2.5" y="3.5" width="8" height="6" fill="none" stroke="var(--brand-blue)" stroke-width="1.2"/><path d="M2.5,3.5 L6.5,7 L10.5,3.5" fill="none" stroke="var(--brand-blue)" stroke-width="1.2"/></svg>
        lewis@briskvitalitypartners.com.au
      </p>
      <p class="contact__row">
        <svg class="contact__icon" viewBox="0 0 13 13"><rect x="0" y="0" width="13" height="13" rx="2" fill="var(--white)"/><circle cx="6.5" cy="6.5" r="4" fill="none" stroke="var(--brand-blue)" stroke-width="1"/><ellipse cx="6.5" cy="6.5" rx="1.8" ry="4" fill="none" stroke="var(--brand-blue)" stroke-width="0.9"/><path d="M2.5,6.5 H10.5" stroke="var(--brand-blue)" stroke-width="0.9"/></svg>
        www.briskvitalitypartners.com.au
      </p>
    </div>
  </section>

</body>
</html>
```